Civic Shieldpoint Company

We have design at www.vexaloft.com and want
New site design
Carallax
Images added
Were looking for your eyes. Just placement and look and feel. No hard coding. Design only.

Industry/Entity Type

It Company

```html
<!DOCTYPE html>
<html lang="en">
<head>
<meta charset="utf-8">
<title>Vexaloft – Civic Shieldpoint Company</title>
<link rel="stylesheet" href="https://fonts.googleapis.com/css2?family=PT+Sans:wght@400;700&display=swap">
<style>
:root{
  --red:#b8141b;
  --red-deep:#a30f15;
  --hero-a:#c9545a;
  --hero-b:#e49a9c;
  --ink:#333333;
  --muted:#555555;
  --line:#d9d9d9;
  --card:#f2f2f2;
  --band:#ebebeb;
  --white:#ffffff;
  --dark:#2b2b2b;
}
*{box-sizing:border-box;margin:0;padding:0}
html,body{width:1200px;height:2548px;overflow:hidden}
body{position:relative;background:var(--white);font-family:"PT Sans",Verdana,sans-serif;color:var(--ink);font-size:14px;line-height:1.4}
.abs{position:absolute}

/* header */
.topbar{left:0;top:0;width:1200px;height:30px;background:#f4f4f4;border-bottom:1px solid #e2e2e2}
.follow{right:138px;top:6px;font-size:13px;color:#444}
.social{top:5px;width:18px;height:18px;background:#5b8ec2;border-radius:2px}
.hero{left:0;top:30px;width:1200px;height:446px;background:linear-gradient(100deg,var(--hero-a) 0%,#d67074 45%,var(--hero-b) 100%);overflow:hidden}
.hero svg{position:absolute;left:0;top:0}
.brandbar{left:0;top:0;width:470px;height:128px;background:var(--white);clip-path:polygon(0 0,100% 0,88% 100%,0 100%)}
.logo{left:200px;top:40px;font-size:38px;font-weight:700;color:var(--dark);letter-spacing:1px}
.logo-mark{left:172px;top:57px;width:20px;height:20px;background:var(--red);border-radius:50%}
.navbar{left:440px;top:30px;width:760px;height:56px;background:var(--white);border-bottom:1px solid #e4e4e4}
.nav{right:200px;top:48px;display:flex;font-size:15px}
.nav a{display:block;padding:0 16px;color:#444;text-decoration:none;border-left:1px solid #ddd}
.nav a:first-child{border-left:0;color:var(--red)}
.welcome{left:198px;top:232px;color:var(--white);font-size:28px;font-weight:400}
.tagline{left:56px;top:274px;width:400px;color:var(--white);font-size:17px;text-align:right;line-height:1.5}
.video{left:560px;top:152px;width:436px;height:268px;border:5px solid var(--white);box-shadow:0 2px 6px rgba(0,0,0,.3);background:linear-gradient(135deg,#c7c3b6,#a9a89e 50%,#d7d2c0)}
.play{left:756px;top:254px;width:56px;height:56px;border-radius:50%;background:rgba(255,255,255,.35)}

/* services */
.card{width:246px;height:304px;border:1px solid var(--line);background:var(--white);padding:9px}
.card-inner{height:100%;background:var(--card);text-align:center;padding:30px 14px 0}
.card svg{display:block;margin:0 auto 18px}
.card h3{font-weight:400;font-size:15px;color:#222;line-height:1.35;margin-bottom:6px;min-height:40px}
.card p{font-size:14px;color:var(--muted);line-height:1.4;height:90px}
.btn{display:inline-block;background:var(--dark);color:var(--white);font-size:13px;padding:8px 18px;margin-top:6px}

/* section heading */
.heading{left:198px;width:796px;display:flex;align-items:center;gap:18px;color:var(--red);font-size:24px;font-weight:400;letter-spacing:1px}
.heading::before,.heading::after{content:"";flex:1;border-top:3px dotted #d0d0d0}

/* table */
.compare{left:198px;top:1214px;width:796px;border-collapse:collapse;font-size:13px;table-layout:fixed}
.compare th{background:var(--red-deep);color:var(--white);font-weight:400;height:46px;border-right:1px solid #c94a4f}
.compare th:first-child{text-align:left;padding-left:18px;font-size:15px;width:168px}
.compare td{text-align:center;height:50px;border:1px solid #e1e1e1;color:#333}
.compare td:first-child{text-align:left;padding-left:18px}
.compare tr:nth-child(odd) td{background:#f3f3f3}
.compare tr:last-child td{height:58px;line-height:1.3}

/* command center */
.intro{left:198px;top:1516px;width:796px;font-size:14px;color:var(--muted)}
.bullets{left:198px;top:1568px;width:796px;list-style:none;font-size:14px;color:var(--muted)}
.bullets li{position:relative;padding-left:22px;line-height:1.4}
.bullets li::before{content:"";position:absolute;left:2px;top:6px;border-left:9px solid var(--red);border-top:5px solid transparent;border-bottom:5px solid transparent}
.band{left:0;top:1712px;width:1200px;height:752px;background:var(--band)}
.shot{background:linear-gradient(180deg,#ffffff 0%,#f1f1f1 60%,#dfe6ec 100%);border:1px solid #cfcfcf;box-shadow:0 1px 4px rgba(0,0,0,.2)}
.steps{font-size:14px;color:var(--muted);line-height:1.35}
.steps p{margin-bottom:14px}
.steps b{font-weight:400;color:var(--red);text-decoration:underline}
.divider{left:540px;top:2110px;width:454px;border-top:2px dotted #bdbdbd}

/* footer */
.footer{left:198px;top:2494px;font-size:13px;color:#333}
.footer a{color:#333;text-decoration:none}
</style>
</head>
<body>

<header>
  <div class="abs topbar"></div>
  <div class="abs follow">Follow Us :</div>
  <span class="abs social" style="right:106px"></span>
  <span class="abs social" style="right:82px"></span>
</header>

<section class="abs hero">
  <svg width="1200" height="446" viewBox="0 0 1200 446" aria-hidden="true">
    <path d="M0 300 Q400 150 1200 60 L1200 446 L0 446Z" fill="#ffffff" opacity=".06"/>
    <path d="M900 446 Q1050 250 1200 200 L1200 446Z" fill="#ffffff" opacity=".12"/>
    <path d="M1060 446 L1200 300 L1200 446Z" fill="#ffffff" opacity=".15"/>
  </svg>
</section>

<div class="abs brandbar"></div>
<span class="abs logo-mark"></span>
<div class="abs logo">Vexaloft</div>
<div class="abs navbar"></div>
<nav class="abs nav"><a href="#">Home</a><a href="#">About Us</a><a href="#">User</a></nav>

<h1 class="abs welcome">Welcome to our site</h1>
<p class="abs tagline">Protect yourself by Vexaloft<br>and feel tensionfree</p>
<div class="abs video" role="img" aria-label="Video still: a stolen driver licence card stamped in red"></div>
<span class="abs play"></span>

<article class="abs card" style="left:198px;top:516px"><div class="card-inner">
  <svg width="40" height="40" viewBox="0 0 40 40" aria-hidden="true"><path d="M6 12l22 -4 3 10 -22 4z" fill="#b8141b"/><rect x="30" y="12" width="5" height="3" fill="#b8141b"/><path d="M13 22l2 7h-8v3h11l-2-11z" fill="#b8141b"/></svg>
  <h3>ID Monitoring &amp;<br>Surveillance</h3>
  <p>engines, human intelligence gathering and mathematical algorithms find and analyze your data online.</p>
  <span class="btn">Read More</span></div></article>

<article class="abs card" style="left:474px;top:516px"><div class="card-inner">
  <svg width="40" height="40" viewBox="0 0 40 40" aria-hidden="true"><text x="20" y="33" text-anchor="middle" font-family="PT Sans,sans-serif" font-weight="700" font-size="36" fill="#b8141b">$</text></svg>
  <h3>$25,000 Loss<br>Insurance</h3>
  <p>Identity Fraud Loss and Expense Reimbursement Master Policy from Marbrook Insurance is designed to...</p>
  <span class="btn">Read More</span></div></article>

<article class="abs card" style="left:750px;top:516px"><div class="card-inner">
  <svg width="40" height="40" viewBox="0 0 40 40" aria-hidden="true"><rect x="6" y="10" width="28" height="22" rx="3" fill="#b8141b"/><rect x="24" y="17" width="12" height="8" rx="2" fill="#8e0f14"/><circle cx="28" cy="21" r="1.6" fill="#fff"/></svg>
  <h3>Lost Wallet<br>Service</h3>
  <p>Store information about the contents of your purse and wallet securely. If ever lost or stolen, you are protected.</p>
  <span class="btn">Read More</span></div></article>

<article class="abs card" style="left:198px;top:842px"><div class="card-inner">
  <svg width="40" height="40" viewBox="0 0 40 40" aria-hidden="true"><rect x="6" y="9" width="28" height="24" rx="2" fill="none" stroke="#b8141b" stroke-width="3"/><rect x="16" y="5" width="8" height="6" fill="#b8141b"/><circle cx="15" cy="19" r="3" fill="#b8141b"/><rect x="10" y="24" width="10" height="4" fill="#b8141b"/><rect x="23" y="18" width="7" height="2" fill="#b8141b"/><rect x="23" y="23" width="7" height="2" fill="#b8141b"/></svg>
  <h3>Identity Theft<br>Recovery</h3>
  <p>If your identity is stolen, we recover your ID for you or assist you in your recovery - your choice.</p>
  <span class="btn">Read More</span></div></article>

<article class="abs card" style="left:474px;top:842px"><div class="card-inner">
  <svg width="40" height="40" viewBox="0 0 40 40" aria-hidden="true"><rect x="5" y="9" width="30" height="22" rx="3" fill="none" stroke="#b8141b" stroke-width="3"/><rect x="5" y="14" width="30" height="4" fill="#b8141b"/><rect x="10" y="23" width="10" height="3" fill="#b8141b"/></svg>
  <h3>ID vs Credit<br>Monitoring</h3>
  <p>Identity scoring and monitoring is more effective than credit report monitoring. Study by Halvern Group.</p>
  <span class="btn">Read More</span></div></article>

<article class="abs card" style="left:750px;top:842px"><div class="card-inner">
  <svg width="40" height="40" viewBox="0 0 40 40" aria-hidden="true"><circle cx="20" cy="11" r="7" fill="#b8141b"/><path d="M7 36 Q8 21 20 21 Q32 21 33 36Z" fill="#b8141b"/><path d="M18 22l2 10 2-10z" fill="#fff"/></svg>
  <h3>Faces of ID<br>Theft</h3>
  <p>Criminals use sophisticated methods to obtain and misuse our personal information.</p>
  <span class="btn">Read More</span></div></article>

<h2 class="abs heading" style="top:1166px">GET STARTED</h2>
<table class="abs compare">
  <tr><th>Compare Protection</th><th>Vexaloft</th><th>Lockwell</th><th>Idenvault</th><th>Keystead ID</th><th>Truvane ID</th><th>ID Sentrywell</th><th>Credora</th></tr>
  <tr><td>Subscription Cost</td><td>$4.15 / mo</td><td>$34.50 / mo</td><td>$35.98 / mo</td><td>$36.95 / mo</td><td>$16.99 / mo</td><td>$39.90 / mo</td><td>$29.90 / mo</td></tr>
  <tr><td>Adults Covered</td><td>All</td><td>2</td><td>2</td><td>2</td><td>2</td><td>2</td><td>2</td></tr>
  <tr><td>Children Covered</td><td>All</td><td>2</td><td>0</td><td>4</td><td>4</td><td>0</td><td>0</td></tr>
  <tr><td>Level of Assistance</td><td>Complete<br>Restoration</td><td>Assisted</td><td>Assisted</td><td>Complete<br>Restoration</td><td>Assisted</td><td>Complete<br>Restoration</td><td>Assisted</td></tr>
</table>

<h2 class="abs heading" style="top:1474px">ID COMMAND CENTER</h2>
<p class="abs intro">The ID Command Center provides a real-time view of your automated identity monitoring and alerts, access to your lost wallet protection, your policy coverage and more.</p>
<ul class="abs bullets">
  <li>View your ID Monitoring and Surveillance status with alerts, and respond to any suspicious information with a click.</li>
  <li>Create and update your Lost Wallet Protection service to be ready when you need it.</li>
  <li>Access to your family Marbrook Personal Loss Policy Coverage including protection description.</li>
  <li>Contact Fully Managed Restoration in the event of suspicious information or ID theft.</li>
  <li>Initiate analysis and as needed, Fully Managed Recovery for you or a family member of any suspicious inquiries or possible identity theft incidents.</li>
</ul>

<div class="abs band"></div>
<div class="abs shot" style="left:200px;top:1750px;width:320px;height:274px" role="img" aria-label="Screenshot of the Privacy Command Center dashboard with callouts 1 to 4"></div>
<div class="abs steps" style="left:540px;top:1744px;width:454px">
  <p>1. <b>Account Status information</b> identifies the type of account, your account ID number and your protection status. In addition, quick view your identity monitoring status results. Green means no new alerts. Red means new alerts found.</p>
  <p>2. <b>Message and task center</b> provides you with notice there are messages to review or tasks that warrant your attention or action. Messages or tasks display here when issued. Subscribers are also emailed new alert notices.</p>
  <p>3. <b>Identity monitoring controls</b> provides subscribers with choices on how to monitor their ID. In addition, more detailed explanation of monitoring, your information being monitored and monitoring history.</p>
  <p>4. <b>Identity theft report</b> submission allows subscribers to file a report if they suspect any activity within their identity that they do not recognize. Reports are reviewed by a specialist. If a true event, a recovery specialist will be assigned to your case. If you suspect you are a victim of identity theft, call the toll-free number immediately.</p>
</div>
<div class="abs divider"></div>

<div class="abs steps" style="left:200px;top:2134px;width:440px">
  <p>5. <b>Lost wallet service setup</b> and update process is there when you need it. If you lose your wallet or purse, call the toll-free number and have a recovery specialist working on your behalf. In addition, set up credit fraud alerts or freeze your credit to eliminate any misuse.</p>
  <p>6. <b>Personal loss insurance</b> coverage details and explanation, subscriber policy number and information, insurance company toll-free number to submit claims and process to monitor claim status.</p>
  <p>7. <b>Red alert notice</b> recognizes there is a new source of information found during the identity monitoring and surveillance. Simply click to view the alert and to provide response.</p>
  <p>8. <b>Red messages or tasks</b> brought to the subscribers attention. Click to review and determine if known information or not. If not, a single click will start the ball rolling to investigate this information further by a recovery specialist.</p>
</div>
<div class="abs shot" style="left:666px;top:2134px;width:328px;height:272px" role="img" aria-label="Screenshot of the Privacy Command Center dashboard with callouts 5 to 8"></div>

<footer class="abs footer"><a href="#">Home</a> | <a href="#">User</a> | <a href="#">Agreement</a> | <a href="#">Privacy Policy</a></footer>

</body>
</html>
```